Building Design company needing a letterhead

We need a letter head for our Building Design company to send letters etc. to our clients, consultants, councils etc. We would like to see our logo used and company colours. I have attached our style guide and an example of our current letterheads. Top left we would like our logo, top right we would like the company details and at the footer we would like some sort of image/design etc. that suits our brand. I like the Torvik Design letterhead attached.

Target Market(s)

Professionals, Councils, Consultants, Mums & Dads

Industry/Entity Type

Architecture

Font styles to use
Other font styles liked:
• refer the design style guide

Colors
f37122
000000
1b1b1b

Requirements
Must have
• Must have the minimum of a logo, company details and footer
Nice to have
• An image/design made for the footer that would suite our brand and website at www.quarvedesign.com.au. Also it would be nice to include the GMKLE logo somewhere perhaps included in the footer.
Should not have
• Large images in the header. I just want the logo and company details.

```html
<!DOCTYPE html>
<html lang="en">
<head>
<meta charset="utf-8">
<title>Quarve Design Letterhead</title>
<link rel="stylesheet" href="https://fonts.googleapis.com/css2?family=Roboto:wght@300;400;700&display=swap">
<style>
  :root {
    --brand-orange: #f37122;
    --brand-black: #000000;
    --brand-charcoal: #1b1b1b;
    --rule-grey: #9a9a9a;
    --text-grey: #4a4a4a;
    --muted-grey: #8a8a8a;
    --paper: #ffffff;
    --ghost: #f6f1ee;
  }
  * { margin: 0; padding: 0; box-sizing: border-box; }
  html, body { width: 848px; height: 1200px; overflow: hidden; background: var(--paper); }
  body { font-family: "Roboto", Arial, sans-serif; font-weight: 300; color: var(--text-grey); }
  .letterhead { position: relative; width: 848px; height: 1200px; overflow: hidden; background: var(--paper); }

  .brand { position: absolute; left: 25px; top: 28px; display: flex; align-items: center; gap: 12px; }
  .brand-square { width: 42px; height: 42px; background: var(--brand-orange); }
  .brand-name { font-weight: 700; font-size: 27px; line-height: 27px; letter-spacing: 1.5px; color: var(--brand-charcoal); text-transform: uppercase; }

  .company-details { position: absolute; left: 26px; top: 101px; font-size: 8.6px; line-height: 11.6px; color: var(--muted-grey); font-weight: 300; }

  .top-rule { position: absolute; left: 243px; top: 47px; width: 570px; height: 2px; background: var(--rule-grey); }
  .top-squares { position: absolute; left: 796px; top: 34px; }
  .top-contacts { position: absolute; left: 247px; top: 56px; display: flex; gap: 38px; font-size: 10px; color: var(--muted-grey); }

  .side-rule { position: absolute; left: 106px; top: 205px; width: 3px; height: 837px; background: var(--brand-orange); }
  .side-marker { position: absolute; left: 96px; top: 195px; }

  .ghost-mark { position: absolute; left: 420px; top: 690px; width: 300px; height: 420px; background: linear-gradient(160deg, var(--ghost), #fbf8f6); }

  .letter { position: absolute; left: 224px; top: 216px; width: 548px; font-size: 15.4px; line-height: 20.5px; color: var(--text-grey); }
  .recipient { margin-bottom: 41px; }
  .letter-date { margin-bottom: 48px; }
  .salutation { margin-bottom: 10px; }
  .letter p.body-text { text-align: justify; hyphens: auto; margin-bottom: 20px; }
  .sign-off { margin-top: 82px; }

  .partner-badge { position: absolute; left: 74px; top: 1060px; display: flex; flex-direction: column; align-items: center; gap: 12px; width: 72px; }
  .partner-shape { width: 56px; height: 56px; background: var(--brand-orange); }
  .partner-name { font-weight: 400; font-size: 15px; letter-spacing: 1px; color: var(--brand-orange); }
</style>
</head>
<body>
<main class="letterhead">
  <header>
    <div class="brand">
      <div class="brand-square"></div>
      <div class="brand-name">Quarve<br>Design</div>
    </div>
    <div class="company-details">
      Unit 3/22 Tarrant Way Halden WA 6214<br>
      PO Box 5172 Halden North WA 6214<br>
      PH (08) 6417 2390<br>
      ABN 41 738 206 514
    </div>
    <div class="top-rule"></div>
    <svg class="top-squares" width="30" height="32" viewBox="0 0 30 32" aria-hidden="true">
      <rect x="8" y="10" width="20" height="20" fill="#9a9a9a"/>
      <rect x="2" y="2" width="20" height="20" fill="var(--brand-charcoal)"/>
    </svg>
    <div class="top-contacts">
      <span>www.quarvedesign.com.au</span>
      <span>admin@quarvedesign.com.au</span>
    </div>
  </header>

  <div class="ghost-mark" aria-hidden="true"></div>

  <div class="side-rule"></div>
  <svg class="side-marker" width="24" height="26" viewBox="0 0 24 26" aria-hidden="true">
    <rect x="8" y="8" width="14" height="16" fill="#7a7a7a"/>
    <rect x="0" y="0" width="16" height="18" fill="var(--brand-orange)"/>
  </svg>

  <article class="letter">
    <div class="recipient">
      Clara Jane Whitlow<br>
      Redgum Building<br>
      41 Farrier Street<br>
      NSW 2051
    </div>
    <div class="letter-date">28th Jan 2016</div>
    <p class="salutation">Dear Ms Whitlow,</p>
    <p class="body-text">I am happy to write a letter of recommendation for Jane Calder in support of her application to the Department of Maternal and Child Health MPH program. Ms. Calder took the classroom version of Principles of Epidemiology for Public Health (EPID 160) this past fall. Based on her performance in the course, I feel she would be a good candidate for the MPH program.</p>
    <p class="body-text">Grading in EPID 160 is based on a combination of “objective” and “subjective” evaluations. The objective components are two open-book, take-home examinations (35% of the overall grade) and a paper (25%), each based on an article. Each teaching assistant grades several exam questions across the entire class (this year we combined the 101 classroom and 64 Internet students). Thus, exam scores provide a good basis for comparison. The papers are also graded anonymously, but in spite of attempts to standardize the grading there are undoubtedly differences across graders.</p>
    <p class="body-text">The more subjective components are TA (20% of the overall grade) and peer (20%) evaluations of participation in small group discussions about case studies based mostly on articles. Although I try to adjust the results for differences in grading styles across TAs and across small groups, these scores are less comparable across the class as a whole.</p>
    <p class="sign-off">
      Yours sincerely,<br>
      Martin L. Hayward, PhD<br>
      Associate Professor
    </p>
  </article>

  <footer class="partner-badge">
    <div class="partner-shape"></div>
    <div class="partner-name">GMKLE</div>
  </footer>
</main>
</body>
</html>
```